New LGBT Nightclub Crowdfunding Poster

We need it to read well for social media posts. All colors should look similar to Seattle’s Sports Teams color schemes.

The top should have: The logo prominently with the fans in the background photo. and then still center and important, "Coming soon!" "You can be part of the first in line for the amazing things happening". (The call to action is the purchase of these amazing deals for the first weekend open / passes. That should be clear).

```html
<!DOCTYPE html>
<html lang="en">
<head>
<meta charset="utf-8">
<title>The Rally – Coming Soon</title>
<link rel="stylesheet" href="https://fonts.googleapis.com/css2?family=Righteous&family=Montserrat:wght@500;700;800&display=swap">
<style>
  :root {
    --backdrop: #e4e6ea;
    --ice-light: #f1f6fb;
    --ice-mid: #c9d9ea;
    --navy: #0e2b6e;
    --navy-deep: #0a2159;
    --forest: #0c6e3a;
    --forest-light: #128a4a;
    --mint: #1fcf7e;
    --mint-deep: #0ea35e;
    --ink-white: #ffffff;
    --crowd: #26345f;
  }
  * { box-sizing: border-box; margin: 0; padding: 0; }
  html, body {
    width: 1200px;
    height: 942px;
    overflow: hidden;
  }
  body {
    background: var(--backdrop);
    font-family: "Montserrat", sans-serif;
  }
  .poster {
    position: absolute;
    left: 295px;
    top: 40px;
    width: 610px;
    height: 862px;
    overflow: hidden;
    box-shadow: 0 10px 30px rgba(0, 0, 0, 0.28);
  }
  .poster-backdrop {
    position: absolute;
    inset: 0;
    width: 610px;
    height: 862px;
  }
  .brand-mark {
    position: absolute;
    left: 225px;
    top: 18px;
    width: 160px;
    height: 215px;
  }
  .brand-name {
    position: absolute;
    left: 0;
    right: 0;
    top: 112px;
    text-align: center;
    font-family: "Montserrat", sans-serif;
    font-weight: 800;
    color: var(--ink-white);
    font-size: 22px;
    line-height: 1.1;
    letter-spacing: 1px;
  }
  .brand-name .district {
    display: block;
    font-size: 12px;
    letter-spacing: 2px;
    margin-top: 22px;
  }
  .headline {
    position: absolute;
    left: 0;
    top: 300px;
    width: 610px;
    height: 270px;
  }
  .pitch {
    position: absolute;
    left: 60px;
    right: 60px;
    top: 582px;
    text-align: center;
    color: var(--ink-white);
    font-weight: 500;
    font-size: 27px;
    line-height: 33px;
  }
  .offer {
    position: absolute;
    left: 57px;
    top: 745px;
    width: 496px;
    height: 102px;
    border: 1.5px solid var(--forest-light);
    border-radius: 12px;
    text-align: center;
  }
  .offer-tag {
    position: absolute;
    left: 50%;
    top: -16px;
    transform: translateX(-50%);
    background: var(--forest);
    color: #d9ffe9;
    font-weight: 700;
    font-size: 19px;
    letter-spacing: 1px;
    padding: 4px 18px;
    border-radius: 16px;
    white-space: nowrap;
  }
  .offer-title {
    margin-top: 24px;
    color: var(--mint);
    font-weight: 800;
    font-size: 46px;
    line-height: 46px;
    letter-spacing: 0.5px;
  }
  .offer-detail {
    margin-top: 4px;
    color: var(--ink-white);
    font-weight: 500;
    font-size: 18.5px;
    letter-spacing: 0.2px;
  }
</style>
</head>
<body>
  <main class="poster">
    <svg class="poster-backdrop" viewBox="0 0 610 862" aria-hidden="true">
      <defs>
        <linearGradient id="ice" x1="0" y1="0" x2="0" y2="1">
          <stop offset="0" stop-color="var(--ice-mid)"/>
          <stop offset="0.55" stop-color="var(--ice-light)"/>
          <stop offset="1" stop-color="var(--ice-mid)"/>
        </linearGradient>
        <linearGradient id="forest-band" x1="0" y1="0" x2="1" y2="1">
          <stop offset="0" stop-color="var(--forest-light)"/>
          <stop offset="1" stop-color="var(--forest)"/>
        </linearGradient>
        <linearGradient id="navy-field" x1="0" y1="0" x2="0" y2="1">
          <stop offset="0" stop-color="var(--navy-deep)"/>
          <stop offset="0.3" stop-color="var(--navy)"/>
          <stop offset="1" stop-color="var(--navy)"/>
        </linearGradient>
      </defs>
      <rect class="sky-field" width="610" height="330" fill="url(#ice)"/>
      <polygon class="forest-band" points="0,189 293,250 0,312" fill="url(#forest-band)"/>
      <polygon class="navy-field" points="0,312 293,250 610,195 610,862 0,862" fill="url(#navy-field)"/>
    </svg>

    <div class="brand-mark" role="img" aria-label="Watercolour crowd of cheering fans with raised arms behind the club name">
      <svg viewBox="0 0 160 215" width="160" height="215" aria-hidden="true">
        <defs>
          <radialGradient id="crowd-wash" cx="0.5" cy="0.6" r="0.6">
            <stop offset="0" stop-color="var(--crowd)"/>
            <stop offset="0.8" stop-color="#34457a"/>
            <stop offset="1" stop-color="#5a6b98" stop-opacity="0"/>
          </radialGradient>
        </defs>
        <ellipse cx="80" cy="130" rx="78" ry="82" fill="url(#crowd-wash)"/>
      </svg>
      <div class="brand-name">THE RALLY<span class="district">PIER NINE</span></div>
    </div>

    <svg class="headline" viewBox="0 0 610 270" aria-label="Coming Soon">
      <defs>
        <linearGradient id="soon-fill" x1="0" y1="0" x2="0" y2="1">
          <stop offset="0" stop-color="var(--mint-deep)"/>
          <stop offset="0.5" stop-color="var(--mint)"/>
          <stop offset="1" stop-color="var(--mint-deep)"/>
        </linearGradient>
      </defs>
      <text x="115" y="110" textLength="428" lengthAdjust="spacingAndGlyphs"
            font-family="Righteous, sans-serif" font-size="124" fill="var(--ink-white)">COMING</text>
      <text x="122" y="250" textLength="424" lengthAdjust="spacingAndGlyphs"
            font-family="Righteous, sans-serif" font-size="178" fill="url(#soon-fill)">SOON</text>
    </svg>

    <p class="pitch">You can be part of the first in line for the amazing things happening</p>

    <section class="offer">
      <span class="offer-tag">PURCHASE OF THESE</span>
      <h2 class="offer-title">AMAZING DEALS</h2>
      <p class="offer-detail">FOR THE FIRST WEEKEND OPEN / PASSES</p>
    </section>
  </main>
</body>
</html>
```